Redcliff Oil & Gas Exploration, LLC

Our website (www.redcliffoilandgas.example) is poorly done and dated. I want to redo it with one main page and wide format photos or oil & gas drilling and production. Perhaps all of the pages listed on the left side of the existing site could be viewed by scrolling down further on the new main page. I want something clean and easy to navigate.

Target Market(s)

Other oil and gas companies and people that we have contacted regarding selling or leasing their mineral rights. These people will come to our website to research our company and become more comfortable doing business with us.

Industry/Entity Type

Oil And Gas

Coding

Coded - Design and coding required

Number of Pages Required

1 page

Font styles to use
Serif

Requirements
Must have
• Clean and uncluttered. Nice, clear wide format picture or oil well or rig and landscape.

```html
<!DOCTYPE html>
<html lang="en">
<head>
<meta charset="utf-8">
<title>Redcliff Oil &amp; Gas Exploration — Contact</title>
<link rel="stylesheet" href="https://fonts.googleapis.com/css2?family=Montserrat:wght@700&family=Lato:wght@400;700&family=Tinos:wght@700&display=swap">
<style>
  :root {
    --nav-orange: #e06300;
    --accent-teal: #1abc9c;
    --ink: #2c3e50;
    --heading: #333333;
    --placeholder: #a9a9a9;
    --rule: #e3e3e3;
    --page-bg: #ededed;
    --white: #ffffff;
  }
  * { box-sizing: border-box; margin: 0; padding: 0; }
  html, body { width: 1200px; height: 675px; overflow: hidden; }
  body {
    position: relative;
    background: radial-gradient(circle at 40% 40%, #f3f3f3 0%, var(--page-bg) 70%, #e6e6e6 100%);
    font-family: "Lato", sans-serif;
  }
  .site-nav {
    position: absolute; left: 0; top: 0;
    width: 1200px; height: 62px;
    background: var(--nav-orange);
  }
  .brand {
    position: absolute; left: 93px; top: 19px;
    font-family: "Montserrat", sans-serif; font-weight: 700;
    font-size: 19px; color: var(--white); letter-spacing: 0.3px;
  }
  .nav-links {
    position: absolute; right: 81px; top: 9px;
    display: flex; list-style: none; height: 44px;
  }
  .nav-links li {
    font-family: "Tinos", serif; font-weight: 700;
    font-size: 13px; letter-spacing: 0.6px; color: var(--white);
    padding: 0 13px; line-height: 44px;
  }
  .nav-links li.is-active { background: var(--accent-teal); padding: 0 14px; }
  .section-title {
    position: absolute; left: 0; top: 80px; width: 1200px;
    text-align: center;
    font-family: "Montserrat", sans-serif; font-weight: 700;
    font-size: 37px; color: var(--heading); letter-spacing: 0.2px;
  }
  .title-divider { position: absolute; left: 489px; top: 125px; }
  .contact-form { position: absolute; left: 258px; top: 173px; width: 689px; }
  .field {
    border-top: 1px solid var(--rule);
    height: 65px;
    padding: 18px 9px 0;
    font-size: 18px; color: var(--placeholder);
  }
  .field-message { height: 180px; border-bottom: 1px solid var(--rule); padding-top: 20px; }
  .send-button {
    display: inline-block; margin: 18px 0 0 9px;
    background: var(--accent-teal); color: var(--white);
    font-weight: 700; font-size: 16px;
    padding: 10px 15px 11px; border-radius: 4px;
  }
</style>
</head>
<body>
  <header class="site-nav">
    <div class="brand">REDCLIFF</div>
    <ul class="nav-links">
      <li>HISTORY</li>
      <li>ABOUT</li>
      <li>FIND US</li>
      <li class="is-active">CONTACT US</li>
    </ul>
  </header>

  <h1 class="section-title">CONTACT US</h1>
  <svg class="title-divider" width="222" height="36" viewBox="0 0 222 36" aria-hidden="true">
    <rect x="0" y="16" width="93" height="4" fill="var(--ink)"/>
    <rect x="129" y="16" width="93" height="4" fill="var(--ink)"/>
    <rect x="93" y="0" width="36" height="36" fill="var(--white)"/>
    <polygon points="111,6 114.2,14.2 122.8,14.6 116,20 118.4,28.4 111,23.6 103.6,28.4 106,20 99.2,14.6 107.8,14.2" fill="var(--ink)"/>
  </svg>

  <form class="contact-form">
    <div class="field">Name</div>
    <div class="field">Email Address</div>
    <div class="field">Phone Number</div>
    <div class="field field-message">Message</div>
    <div class="send-button">Send</div>
  </form>
</body>
</html>
```